Lanterns Over Harbor Gate: Notes on Quiet Ambition

I need a book cover. The genre is self-help. would like something that looks original. The book is a barber's story. A barber who earns an M.B.A. I don't mind some type of scissor but I do not want it held to a cosmetology market. Something that speaks to everyone. No stock images. Format 4.25" x 7" This is what book printers call a pocket book.

Requirements
Must have
• Original cover. No stock images.
Nice to have
• I like scissors. Maybe stick men. Creativity
Should not have
• No Stock Images. No Clippers

```html
<!DOCTYPE html>
<html lang="en">
<head>
<meta charset="utf-8">
<title>Lanterns Over Harbor Gate — Cover</title>
<link rel="stylesheet" href="https://fonts.googleapis.com/css2?family=Amatic+SC:wght@700&family=Oswald:wght@300&display=swap">
<style>
  :root {
    --paper: #fcf8f3;
    --ink: #1a1a1a;
    --orange: #f39a2a;
    --red: #e2264a;
    --magenta: #c3195c;
    --plum: #7a3a78;
    --slate: #445a7a;
    --teal: #1fa88a;
  }
  html, body {
    margin: 0;
    padding: 0;
    overflow: hidden;
    background: var(--paper);
  }
  .cover {
    position: relative;
    width: 729px;
    height: 1200px;
    overflow: hidden;
    background: var(--paper);
  }
  .cover__artwork {
    position: absolute;
    inset: 0;
    width: 729px;
    height: 1200px;
  }
  .cover__subtitle {
    position: absolute;
    top: 74px;
    right: 43px;
    margin: 0;
    font-family: "Oswald", sans-serif;
    font-weight: 300;
    font-size: 36px;
    line-height: 1;
    color: var(--ink);
  }
  .cover__title {
    position: absolute;
    top: 458px;
    right: 313px;
    margin: 0;
    text-align: right;
    font-family: "Amatic SC", cursive;
    font-weight: 700;
    line-height: 0.95;
    background: linear-gradient(180deg, var(--magenta) 0%, var(--plum) 70%, var(--slate) 100%);
    -webkit-background-clip: text;
    background-clip: text;
    color: transparent;
    white-space: nowrap;
  }
  .cover__title-line {
    display: block;
  }
  .cover__title-line--top { font-size: 92px; }
  .cover__title-line--bottom { font-size: 84px; }
  .cover__author {
    position: absolute;
    top: 1052px;
    left: 0;
    width: 729px;
    margin: 0;
    text-align: center;
    font-family: "Amatic SC", cursive;
    font-weight: 700;
    font-size: 56px;
    letter-spacing: 0.62em;
    text-indent: 0.62em;
    color: var(--ink);
  }
</style>
</head>
<body>
  <main class="cover">
    <svg class="cover__artwork" viewBox="0 0 729 1200" role="img" aria-label="Line drawing of open scissors sweeping diagonally from the top left to the right edge, coloured in a gradient from orange through red and purple to teal">
      <defs>
        <linearGradient id="scissor-tones" x1="0" y1="0" x2="1" y2="1">
          <stop offset="0" stop-color="var(--orange)"/>
          <stop offset="0.35" stop-color="var(--red)"/>
          <stop offset="0.6" stop-color="var(--plum)"/>
          <stop offset="1" stop-color="var(--teal)"/>
        </linearGradient>
      </defs>
      <path d="M0 0 L250 0 L400 200 L470 290 L729 255 L729 760 L600 770 L470 700 L455 470 L360 350 L0 140 Z"
            fill="url(#scissor-tones)" opacity="0.28"/>
    </svg>

    <p class="cover__subtitle">Notes on Quiet Ambition</p>

    <h1 class="cover__title">
      <span class="cover__title-line cover__title-line--top">Lanterns Over</span>
      <span class="cover__title-line cover__title-line--bottom">Harbor Gate</span>
    </h1>

    <p class="cover__author">Author Name</p>
  </main>
</body>
</html>
```